apparel brand store for hero type shirt

we need a website design for a new apparel compagny basend in montreal called '' ateliervoransol '' . We design innovative yet simple artwork for the city .we would like to get a MINIMALISTE soft color website . The design most communicate ' MUSUEM '' feeling.
simple looking but looking UPMARKET .
i dont have any exemple i really want you to focus on
( apparel + musuem looking + upmarket )

Requirements
Must have
• white backgroung with a little bit of ( orange / dark green and grey camo )
-the came as to be 5 to 10% transparant
Nice to have
• go fallow on ig
Should not have
• BRIGHT COLOURS

```html
<!DOCTYPE html>
<html lang="en">
<head>
<meta charset="utf-8">
<title>Atelier Voransol — Apparel</title>
<link href="https://fonts.googleapis.com/css2?family=Poppins:wght@400;500;600;700&family=Karla:wght@400;500;700&display=swap" rel="stylesheet">
<style>
  :root {
    --accent: #e8461f;
    --accent-dark: #c9381a;
    --ink: #1c1c1c;
    --body: #3a3a3a;
    --nav-active: #2e7fb8;
    --muted: #6b6b6b;
    --white: #ffffff;
    --blog-bg: #f3f1f1;
    --footer-bg: #2b2b2b;
    --footer-text: #d9d9d9;
    --footer-line: #4a4a4a;
  }
  * { box-sizing: border-box; margin: 0; padding: 0; }
  html, body { width: 1200px; height: 4193px; overflow: hidden; background: var(--white); }
  body { font-family: "Karla", sans-serif; color: var(--body); position: relative; }
  .abs { position: absolute; }
  .heading { font-family: "Poppins", sans-serif; }

  /* Header */
  .site-header { left: 0; top: 0; width: 1200px; height: 72px; background: var(--white); }
  .brand { left: 130px; top: 18px; font-family: "Poppins", sans-serif; font-weight: 700; font-size: 27px; color: var(--ink); letter-spacing: -0.3px; }
  .main-nav { left: 457px; top: 30px; display: flex; gap: 30px; font-family: "Poppins", sans-serif; font-size: 12.5px; color: var(--ink); }
  .main-nav .active { color: var(--nav-active); text-decoration: underline; font-weight: 600; }
  .utility { left: 893px; top: 30px; display: flex; align-items: center; gap: 9px; font-size: 11.5px; color: var(--muted); font-family: "Poppins", sans-serif; }
  .utility svg { display: block; }

  /* Hero */
  .hero { left: 0; top: 72px; width: 1200px; height: 646px; background: radial-gradient(ellipse at 55% 40%, #8a7a63 0%, #5c4c3c 50%, #3a2f25 100%); }
  .hero-title { left: 84px; top: 292px; font-family: "Poppins", sans-serif; font-weight: 700; font-size: 40px; color: var(--white); letter-spacing: 0.5px; }
  .hero-sub { left: 84px; top: 360px; font-family: "Poppins", sans-serif; font-size: 16.5px; line-height: 21px; color: var(--white); }
  .btn { display: flex; align-items: center; justify-content: center; background: var(--accent); color: var(--white); font-family: "Poppins", sans-serif; font-weight: 500; }
  .hero-btn { left: 85px; top: 428px; width: 150px; height: 47px; font-size: 18px; }
  .hero-arrows { left: 1104px; top: 652px; display: flex; gap: 12px; }

  /* Section titles */
  .section-title { left: 0; width: 1200px; text-align: center; font-family: "Poppins", sans-serif; font-weight: 700; font-size: 25px; color: var(--ink); }
  .title-rule { left: 577px; width: 46px; height: 2px; background: var(--accent); }

  .photo { display: block; }
  .card-label { text-align: center; font-family: "Poppins", sans-serif; font-weight: 600; font-size: 13.5px; color: var(--ink); }
  .card-text { text-align: center; font-size: 13.5px; line-height: 20px; color: var(--body); }
  .card-btn { height: 35px; font-size: 13.5px; }

  .product-name { font-family: "Poppins", sans-serif; font-weight: 600; font-size: 11.5px; color: var(--ink); }
  .product-price { font-family: "Poppins", sans-serif; font-weight: 600; font-size: 14px; color: var(--accent-dark); }

  /* Promo */
  .promo { left: 0; top: 1815px; width: 1200px; height: 525px; background: linear-gradient(90deg, #2b2622 0%, #3f3530 20%, #6a2a35 45%, #5f5438 55%, #7a2540 70%, #3d3138 85%, #2a2624 100%); }
  .promo-text { left: 0; top: 1995px; width: 1200px; text-align: center; font-family: "Poppins", sans-serif; font-weight: 700; font-size: 47px; line-height: 52px; color: var(--white); }

  /* Testimonial */
  .quote { left: 330px; top: 2470px; width: 540px; text-align: center; font-size: 16px; line-height: 22.5px; color: var(--body); }
  .quote-name { left: 0; top: 2614px; width: 1200px; text-align: center; font-family: "Poppins", sans-serif; font-weight: 600; font-size: 14px; color: var(--ink); }

  /* Best sellers */
  .camo-band { left: 0; top: 2683px; width: 1200px; height: 583px; background: radial-gradient(ellipse at 15% 30%, #c9c9c9 0%, transparent 40%), radial-gradient(ellipse at 70% 70%, #cfcfcf 0%, transparent 45%), radial-gradient(ellipse at 90% 20%, #d4d4d4 0%, transparent 35%), #e3e3e3; }
  .seller-card { background: var(--white); }

  /* Blog */
  .blog-band { left: 0; top: 3266px; width: 1200px; height: 604px; background: var(--blog-bg); }
  .blog-card { background: var(--white); }
  .blog-title { font-family: "Poppins", sans-serif; font-weight: 700; font-size: 14.5px; color: var(--ink); }
  .blog-text { font-size: 13.5px; line-height: 17.5px; color: var(--body); }
  .read-more { font-family: "Poppins", sans-serif; font-weight: 600; font-size: 11.5px; color: var(--accent-dark); text-decoration: underline; }

  /* Footer */
  .site-footer { left: 0; top: 3870px; width: 1200px; height: 323px; background: var(--footer-bg); }
  .footer-heading { font-family: "Poppins", sans-serif; font-weight: 600; font-size: 15px; color: var(--white); }
  .footer-text { font-size: 13.5px; line-height: 20.5px; color: var(--footer-text); }
  .footer-menu { list-style: none; font-family: "Poppins", sans-serif; font-size: 13px; line-height: 21.5px; color: var(--footer-text); }
  .signup { left: 724px; top: 3994px; width: 341px; height: 45px; border: 1px solid #8a8a8a; display: flex; }
  .signup-field { flex: 1; padding-left: 18px; display: flex; align-items: center; font-size: 12px; color: var(--footer-text); }
  .signup-go { width: 46px; border-left: 1px solid #8a8a8a; display: flex; align-items: center; justify-content: center; }
  .footer-rule { left: 132px; top: 4096px; width: 933px; height: 1px; background: var(--footer-line); }
  .copyright { left: 0; top: 4137px; width: 1200px; text-align: center; font-size: 12px; color: var(--footer-text); }
</style>
</head>
<body>

<header class="abs site-header">
  <div class="abs brand">Atelier Voransol</div>
  <nav class="abs main-nav">
    <span class="active">HOME</span><span>ABOUT US</span><span>PRODUCTS</span><span>BLOG</span><span>CONTACT US</span>
  </nav>
  <div class="abs utility">
    <svg width="11" height="11" viewBox="0 0 11 11"><circle cx="4.5" cy="4.5" r="3.3" fill="none" stroke="#333" stroke-width="1.6"/><line x1="7" y1="7" x2="10" y2="10" stroke="#333" stroke-width="1.6"/></svg>
    <span>Account</span><span>USD $</span>
    <svg width="16" height="15" viewBox="0 0 16 15"><rect x="1.5" y="4" width="13" height="10" fill="none" stroke="#555" stroke-width="1.3"/><path d="M5 4 V2.5 a3 2 0 0 1 6 0 V4" fill="none" stroke="#555" stroke-width="1.3"/></svg>
    <span>Cart (0)</span>
  </div>
</header>

<section class="abs hero" role="img" aria-label="Two mannequins dressed in shirts, a white skirt and white trousers with a leather bag"></section>
<h1 class="abs hero-title">APPAREL</h1>
<p class="abs hero-sub">LOREM IPSUM IS SIMPLY<br>DUMMY TEXT OF THE PRINTING</p>
<div class="abs btn hero-btn">SHOP NOW</div>
<div class="abs hero-arrows">
  <svg width="16" height="20" viewBox="0 0 16 20"><path d="M11 3 L4 10 L11 17" fill="none" stroke="#fff" stroke-width="2.5"/></svg>
  <svg width="16" height="20" viewBox="0 0 16 20"><path d="M5 3 L12 10 L5 17" fill="none" stroke="#fff" stroke-width="2.5"/></svg>
</div>

<!-- Categories -->
<h2 class="abs section-title" style="top:758px">CATEGORIES</h2>
<div class="abs title-rule" style="top:805px"></div>

<div class="abs photo" style="left:132px;top:843px;width:301px;height:227px;background:linear-gradient(160deg,#b9b9b9,#8d8d8d)" role="img" aria-label="Mannequin in a straw hat and a two-tone women's top"></div>
<div class="abs photo" style="left:449px;top:843px;width:301px;height:227px;background:linear-gradient(160deg,#b5b5b5,#8a8a8a)" role="img" aria-label="Mannequin in a dark hat and a blue striped men's shirt"></div>
<div class="abs photo" style="left:770px;top:843px;width:301px;height:227px;background:linear-gradient(160deg,#bcbcbc,#909090)" role="img" aria-label="Mannequin in a straw hat and a black striped t-shirt"></div>

<div class="abs card-label" style="left:132px;top:1099px;width:301px">FOR WOMEN</div>
<div class="abs card-label" style="left:449px;top:1099px;width:301px">FOR MEN</div>
<div class="abs card-label" style="left:770px;top:1099px;width:301px">T SHIRTS</div>
<p class="abs card-text" style="left:132px;top:1133px;width:301px">Lorem Ipsum is simply dummy text of the<br>printing and typesetting industry.</p>
<p class="abs card-text" style="left:449px;top:1133px;width:301px">Lorem Ipsum is simply dummy text of the<br>printing and typesetting industry.</p>
<p class="abs card-text" style="left:770px;top:1133px;width:301px">Lorem Ipsum is simply dummy text of the<br>printing and typesetting industry.</p>
<div class="abs btn card-btn" style="left:231px;top:1196px;width:111px">SHOP NOW</div>
<div class="abs btn card-btn" style="left:544px;top:1196px;width:111px">SHOP NOW</div>
<div class="abs btn card-btn" style="left:868px;top:1196px;width:111px">SHOP NOW</div>

<!-- Recommended -->
<h2 class="abs section-title" style="top:1310px">RECOMMENDED FOR YOU</h2>
<div class="abs title-rule" style="top:1357px"></div>

<div class="abs photo" style="left:132px;top:1405px;width:223px;height:296px;background:linear-gradient(170deg,#b3b3b3,#6e5355)" role="img" aria-label="Mannequin in a dark red ombre dress"></div>
<div class="abs photo" style="left:376px;top:1405px;width:223px;height:296px;background:linear-gradient(170deg,#c3c3c3,#9a9a7a)" role="img" aria-label="Mannequin in a bright striped top and white trousers"></div>
<div class="abs photo" style="left:612px;top:1405px;width:223px;height:296px;background:linear-gradient(170deg,#d0d0d0,#8e7b74)" role="img" aria-label="Mannequin in a patterned blouse and brown shorts"></div>
<div class="abs photo" style="left:847px;top:1405px;width:223px;height:296px;background:linear-gradient(170deg,#a9a9b3,#34405e)" role="img" aria-label="Mannequin in a blue striped top and jeans with a bag"></div>

<div class="abs product-name" style="left:132px;top:1719px">LOREM IPSUM IS SIMPLY</div>
<div class="abs product-name" style="left:376px;top:1719px">LOREM IPSUM IS SIMPLY</div>
<div class="abs product-name" style="left:612px;top:1719px">LOREM IPSUM IS SIMPLY</div>
<div class="abs product-name" style="left:847px;top:1719px">LOREM IPSUM IS SIMPLY</div>
<div class="abs product-price" style="left:132px;top:1738px">$25.00</div>
<div class="abs product-price" style="left:376px;top:1738px">$25.00</div>
<div class="abs product-price" style="left:612px;top:1738px">$25.00</div>
<div class="abs product-price" style="left:847px;top:1738px">$25.00</div>

<!-- Promo -->
<section class="abs promo" role="img" aria-label="Row of mannequins in colourful jackets and scarves inside a clothing store"></section>
<div class="abs promo-text">10% OFF<br>NEW PRODUCTS</div>

<!-- Testimonials -->
<h2 class="abs section-title" style="top:2382px">TESTIMONIALS</h2>
<div class="abs title-rule" style="top:2427px"></div>
<p class="abs quote">At vero eos et accusamus et iusto odio dignissimos ducimus qui blanditiis praesentium voluptatum deleniti atque corrupti quos dolores et quas molestias excepturi sint occaecati cupiditate non provident, similique sunt in culpa qui officia deserunt mollitia animi, id est laborum et dolorum fuga. Et harum quidem rerum facilis est et expedita</p>
<div class="abs quote-name">MARGAUX</div>

<!-- Best sellers -->
<section class="abs camo-band" role="img" aria-label="Soft grey camouflage background"></section>
<h2 class="abs section-title" style="top:2727px">BEST SELLERS</h2>
<div class="abs title-rule" style="top:2773px"></div>

<div class="abs seller-card" style="left:132px;top:2820px;width:301px;height:413px"></div>
<div class="abs seller-card" style="left:449px;top:2820px;width:301px;height:413px"></div>
<div class="abs seller-card" style="left:770px;top:2820px;width:301px;height:413px"></div>
<div class="abs photo" style="left:132px;top:2820px;width:301px;height:224px;background:linear-gradient(160deg,#8e8e96,#c07a2a)" role="img" aria-label="Mannequin in a black hat and an orange knit sweater"></div>
<div class="abs photo" style="left:449px;top:2820px;width:301px;height:224px;background:linear-gradient(160deg,#b4b4b8,#56596e)" role="img" aria-label="Mannequin in a dark hat and a navy ruffled dress"></div>
<div class="abs photo" style="left:770px;top:2820px;width:301px;height:224px;background:linear-gradient(160deg,#b0b0b0,#3f5a4e)" role="img" aria-label="Mannequin in a green and leopard print blouse"></div>

<div class="abs card-label" style="left:132px;top:3073px;width:301px">LOREM IPSUM IS SIMPLY</div>
<div class="abs card-label" style="left:449px;top:3073px;width:301px">LOREM IPSUM IS SIMPLY</div>
<div class="abs card-label" style="left:770px;top:3073px;width:301px">LOREM IPSUM IS SIMPLY</div>
<p class="abs card-text" style="left:132px;top:3107px;width:301px">Lorem Ipsum is simply dummy text of the<br>printing and typesetting industry.</p>
<p class="abs card-text" style="left:449px;top:3107px;width:301px">Lorem Ipsum is simply dummy text of the<br>printing and typesetting industry.</p>
<p class="abs card-text" style="left:770px;top:3107px;width:301px">Lorem Ipsum is simply dummy text of the<br>printing and typesetting industry.</p>
<div class="abs btn card-btn" style="left:224px;top:3170px;width:117px">SHOP NOW</div>
<div class="abs btn card-btn" style="left:541px;top:3170px;width:117px">SHOP NOW</div>
<div class="abs btn card-btn" style="left:868px;top:3170px;width:117px">SHOP NOW</div>

<!-- Blog -->
<section class="abs blog-band"></section>
<h2 class="abs section-title" style="top:3313px">LATEST BLOG</h2>
<div class="abs title-rule" style="top:3358px"></div>

<div class="abs blog-card" style="left:133px;top:3404px;width:289px;height:409px"></div>
<div class="abs blog-card" style="left:454px;top:3404px;width:290px;height:409px"></div>
<div class="abs blog-card" style="left:777px;top:3404px;width:288px;height:409px"></div>
<div class="abs photo" style="left:133px;top:3404px;width:289px;height:223px;background:linear-gradient(160deg,#a7a7a7,#7a6a3e)" role="img" aria-label="Mannequin in a sheer olive blouse"></div>
<div class="abs photo" style="left:454px;top:3404px;width:290px;height:223px;background:linear-gradient(160deg,#7c7c7c,#1e1e1e)" role="img" aria-label="Dark mannequin in a black and cream patterned top"></div>
<div class="abs photo" style="left:777px;top:3404px;width:288px;height:223px;background:linear-gradient(160deg,#a9a9a9,#7d6a5e)" role="img" aria-label="Mannequin in a taupe top with a printed scarf"></div>

<div class="abs blog-title" style="left:159px;top:3650px">LOREM IPSUM DOLOR SIT</div>
<div class="abs blog-title" style="left:480px;top:3650px">LOREM IPSUM DOLOR SIT</div>
<div class="abs blog-title" style="left:802px;top:3650px">LOREM IPSUM DOLOR SIT</div>
<p class="abs blog-text" style="left:159px;top:3684px;width:240px">Lorem Ipsum is simply dummy texte printing and typesetting industry. quasi architecto beatae vitae dicta explicabo. Nemo enim ipsam</p>
<p class="abs blog-text" style="left:480px;top:3684px;width:240px">Lorem Ipsum is simply dummy texte printing and typesetting industry. quasi architecto beatae vitae dicta explicabo. Nemo enim ipsam</p>
<p class="abs blog-text" style="left:802px;top:3684px;width:240px">Lorem Ipsum is simply dummy texte printing and typesetting industry. quasi architecto beatae vitae dicta explicabo. Nemo enim ipsam</p>
<div class="abs read-more" style="left:159px;top:3767px">READ MORE</div>
<div class="abs read-more" style="left:480px;top:3767px">READ MORE</div>
<div class="abs read-more" style="left:802px;top:3767px">READ MORE</div>

<!-- Footer -->
<footer class="abs site-footer"></footer>
<div class="abs footer-heading" style="left:132px;top:3914px">ABOUT</div>
<div class="abs footer-heading" style="left:498px;top:3914px">MENU</div>
<div class="abs footer-heading" style="left:724px;top:3914px">STAY CONNECTED</div>
<p class="abs footer-text" style="left:132px;top:3953px;width:285px">Lorem Ipsum is simply dummy text of the printing and typesetting industry. veritatis et qai architecto beatae vitae dicta sunt explicabo. Nemo enim ipsam</p>
<ul class="abs footer-menu" style="left:498px;top:3949px">
  <li>HOME</li><li>PRICING</li><li>HOW IT WORKS</li><li>GIFT BOXES</li><li>CONTACT US</li>
</ul>
<p class="abs footer-text" style="left:724px;top:3949px">Join our mailing list to get updates</p>
<div class="abs signup">
  <div class="signup-field">E mail address</div>
  <div class="signup-go"><svg width="12" height="18" viewBox="0 0 12 18"><path d="M3 3 L9 9 L3 15" fill="none" stroke="#fff" stroke-width="1.6"/></svg></div>
</div>
<div class="abs footer-rule"></div>
<div class="abs copyright">Copyright © 2020 All Rights Reserved</div>

</body>
</html>
```